Company brochure

I would like to redesign our existing brochure.
It shall be trifold brochure with more modern and better appealing design than the old one. I am uploading the old one. The new design shall have all all information repeated from old brochure. It could be more or less pictures. I will provide more pictures if required. The keep text is important, the font shall be more modern. Brochure size shall be trifoldt US Legal size paper 8.5" x 14". I will provide all pitures, logos etc in a original format after design concept will be established or before on request.

Industry/Entity Type

It Company

Font styles to use
Other font styles liked:
• calibri

Colors
0555a3
3176b5
85abd2
0692cd
33a6d7
85cae6
1ab09a
33b8a4
87cfc6

Requirements
Nice to have
• I need all information from existing brochure such as text, customer logos, professional assos. logos to be shown in a new one. Picture could be added more.
Should not have
• No changes allowed to company letterhead. Only slight modifications allowed to company logo

```html
<!DOCTYPE html>
<html lang="en">
<head>
<meta charset="utf-8">
<title>Summit Cooling & Air Systems – Trifold Brochure</title>
<link href="https://fonts.googleapis.com/css2?family=Open+Sans:wght@400;600;700&display=swap" rel="stylesheet">
<style>
:root{
  --stage:#3b3b3b;
  --brand-blue:#2d6897;
  --deep-blue:#1d5a8e;
  --sky:#85cae6;
  --teal:#1fab96;
  --ink:#3a3a3a;
  --white:#ffffff;
}
*{margin:0;padding:0;box-sizing:border-box}
html,body{width:1200px;height:1200px;overflow:hidden;background:var(--stage)}
body{font-family:"Open Sans",Calibri,sans-serif;position:relative}
.spread{position:absolute;left:177px;width:846px;height:514px;overflow:hidden}
.spread--outer{top:64px;background:var(--brand-blue)}
.spread--inner{top:617px;background:var(--white)}
.abs{position:absolute}
.shapes{position:absolute;left:0;top:0}

/* outer spread */
.facts h3{color:var(--white);font-size:10.4px;font-weight:600;line-height:12px;letter-spacing:.3px}
.facts p{color:var(--white);font-size:7.2px;font-weight:600;line-height:12.8px;text-align:justify;margin-top:6px}
.facts ul{list-style:none;margin-top:4px}
.facts li{color:var(--white);font-size:7px;line-height:12.6px}
.facts li::before{content:"•";margin-right:5px}
.quote{color:var(--white);font-size:11.5px;font-weight:600;line-height:14.5px;letter-spacing:.4px}
.contact{left:282px;top:118px;width:282px;text-align:center;color:var(--white)}
.contact .name{font-size:11.8px;font-weight:600;line-height:18px;letter-spacing:.4px}
.contact .addr{margin-top:22px;font-size:11.6px;line-height:17.6px}
.contact .addr b{font-weight:700}
.contact hr{width:136px;margin:8px auto 9px;border:0;border-top:1px solid rgba(255,255,255,.8)}
.contact .lic{font-size:11.6px}
.web{left:282px;top:482px;width:282px;text-align:center;color:var(--deep-blue);font-size:11.6px;font-weight:700;letter-spacing:.3px}
.brand{left:595px;top:60px;display:flex;align-items:center;gap:12px;color:var(--white)}
.brand .mark{width:30px;height:30px;background:var(--white)}
.brand span{font-size:11.5px;font-weight:700;line-height:13px;letter-spacing:.3px}
.offer{left:612px;top:418px;display:flex;gap:12px;align-items:flex-start}
.offer .mark{width:22px;height:22px;background:var(--deep-blue);margin-top:8px}
.offer ul{list-style:none}
.offer li{color:var(--deep-blue);font-size:9.6px;font-weight:600;line-height:12.6px;letter-spacing:.4px}

/* inner spread */
.inner-title{font-size:10.4px;font-weight:600;color:var(--deep-blue);letter-spacing:.4px;line-height:12px}
.inner-title--light{color:var(--white)}
.body-copy{font-size:7px;line-height:12.6px;color:var(--ink);text-align:justify}
.bullets{list-style:none}
.bullets li{font-size:7px;line-height:12.6px;color:var(--ink);padding-left:10px;position:relative}
.bullets li::before{content:"•";position:absolute;left:0}
.checks{list-style:none}
.checks li{font-size:7px;line-height:12.6px;padding-left:14px;position:relative;text-align:justify}
.checks li::before{content:"✓";position:absolute;left:0;font-size:7.5px}
.checks--light li{color:var(--white);font-weight:600}
.checks--dark li{color:var(--ink)}
.checks .hl{color:var(--teal)}
.service-panel{left:282px;top:0;width:282px;height:391px;background:var(--brand-blue)}
.emergency{left:457px;top:31px;width:107px;height:46px;background:var(--white);display:flex;align-items:center;gap:8px;padding-left:10px}
.emergency span{font-size:8.3px;font-weight:700;line-height:10px;color:var(--deep-blue)}
.clients{left:596px;top:288px;width:230px;display:grid;grid-template-columns:repeat(5,1fr);row-gap:17px;column-gap:2px}
.clients span{font-size:7.4px;font-weight:700;color:var(--deep-blue);text-align:center;line-height:9px}
.promise{left:594px;top:430px;width:219px;height:84px;background:var(--teal);color:var(--white);text-align:center;padding-top:12px}
.promise p{font-size:11px;font-weight:600;line-height:13.5px;letter-spacing:.4px}
.promise .url{font-size:9.6px;margin-top:6px;font-weight:600}
</style>
</head>
<body>

<!-- Outer spread -->
<section class="spread spread--outer">
  <svg class="shapes" width="846" height="514" viewBox="0 0 846 514">
    <defs>
      <linearGradient id="plantTone" x1="0" y1="0" x2="1" y2="1">
        <stop offset="0" stop-color="#8fb8dc"/>
        <stop offset=".5" stop-color="#3d5a6a"/>
        <stop offset="1" stop-color="#b9c0c4"/>
      </linearGradient>
    </defs>
    <polygon points="49.6,432 266,432 183,477 49.6,477" fill="var(--teal)"/>
    <polygon points="183,477 266,432 285,432 201,477" fill="var(--teal)" opacity=".5"/>
    <polygon points="479.2,316 846,113.6 846,408" fill="url(#plantTone)" role="img" aria-label="Photo of an industrial refrigeration compressor room with blue piping"/>
    <polygon points="115.2,514 479.2,316 846,408 846,514" fill="var(--white)"/>
    <circle cx="345" cy="428" r="24" fill="none" stroke="var(--deep-blue)" stroke-width="3"/>
    <circle cx="422" cy="428" r="28" fill="var(--deep-blue)"/>
    <rect x="472" y="410" width="52" height="34" fill="#2f8a3c"/>
  </svg>

  <div class="facts abs" style="left:33px;top:38px;width:234px">
    <h3>REFRIGERATION<br>FACILITIES SERVICED</h3>
    <p>Food processing, cold storages and distribution facilities, meat and poultry processing plants, bakeries, dairies, beverage bottling facilities, ice production, chemical plants, refineries and ice rinks.</p>
  </div>
  <div class="facts abs" style="left:33px;top:138px;width:234px">
    <h3>INDUSTRIAL &amp; COMMERCIAL<br>HVAC FACILITIES SERVICED</h3>
    <p>Production plant and manufacturing facilities, distribution and storage warehouses, office buildings, data centers, hospitals, colleges, shopping malls and country clubs.</p>
  </div>
  <div class="facts abs" style="left:33px;top:237px;width:250px">
    <h3>CONSTRUCTION</h3>
    <ul>
      <li>Ammonia &amp; freon refrigeration build-up systems.</li>
      <li>Refrigeration and HVAC equipment changeover.</li>
      <li>Freon packaged condensing units and chillers.</li>
      <li>Blast freezers, spiral and tunnel freezers.</li>
      <li>Computerized control, control and power wiring.</li>
      <li>Build-up glycol and water chillers.</li>
      <li>Air handlers and evaporators.</li>
      <li>Refrigeration, glycol, chill water and process piping.</li>
      <li>Certified X-ray quality welding.</li>
      <li>Carbon steel, stainless steel, copper, PVC and sanitary piping.</li>
      <li>Hot tapping available.</li>
    </ul>
  </div>
  <div class="quote abs" style="left:59px;top:440px">GET A FREE<br>QUOTE &amp; SURVEY!</div>

  <div class="contact abs">
    <div class="name">SUMMIT COOLING<br>&amp; AIR SYSTEMS</div>
    <div class="addr">4180 Harlow Avenue<br>Westbrook, CA 91800<br><b>P: 626-555-0142</b><br>F: 626-555-0143</div>
    <hr>
    <div class="lic">Lic. # 742318</div>
  </div>
  <div class="web abs">www.summitcoolair.com</div>

  <div class="brand abs"><div class="mark"></div><span>SUMMIT COOLING<br>&amp; AIR SYSTEMS</span></div>
  <div class="offer abs">
    <div class="mark"></div>
    <ul>
      <li>INDUSTRIAL &amp; COMMERCIAL</li>
      <li>AMMONIA &amp; FREON</li>
      <li>SERVICE &amp; MAINTENANCE</li>
      <li>DESIGN &amp; ENGINEERING</li>
      <li>CONSTRUCTION</li>
    </ul>
  </div>
</section>

<!-- Inner spread -->
<section class="spread spread--inner">
  <svg class="shapes" width="846" height="514" viewBox="0 0 846 514">
    <defs>
      <linearGradient id="warehouseTone" x1="0" y1="0" x2="0" y2="1">
        <stop offset="0" stop-color="#d8dde0"/><stop offset=".6" stop-color="#9aa6ae"/><stop offset="1" stop-color="#4d5a66"/>
      </linearGradient>
      <linearGradient id="skyTone" x1="0" y1="0" x2="0" y2="1">
        <stop offset="0" stop-color="#9fc6e6"/><stop offset=".7" stop-color="#dbe9f3"/><stop offset="1" stop-color="#7c8a96"/>
      </linearGradient>
      <linearGradient id="draftTone" x1="0" y1="0" x2="1" y2="1">
        <stop offset="0" stop-color="#eef2f6"/><stop offset=".6" stop-color="#d9e3ec"/><stop offset="1" stop-color="#c9d3dc"/>
      </linearGradient>
    </defs>
    <rect x="168" y="0" width="114" height="238" fill="url(#warehouseTone)" role="img" aria-label="Photo of a cold storage warehouse interior with loading dock doors"/>
    <rect x="0" y="238" width="105" height="276" fill="url(#skyTone)" role="img" aria-label="Photo of a helicopter lifting equipment above a city skyline"/>
    <rect x="282" y="391" width="282" height="123" fill="url(#draftTone)" role="img" aria-label="Photo of hands drafting engineering plans with pencil and ruler"/>
  </svg>

  <div class="inner-title abs" style="left:39px;top:38px">EXPERIENCE</div>
  <p class="body-copy abs" style="left:36px;top:61px;width:115px">Thirty plus years in industrial, commercial, ammonia and freon refrigeration and air conditioning. Experienced in all aspects of refrigeration projects, from design concept through execution, with the ability to cost-effectively satisfy customer requirements within aggressive time frames.</p>

  <div class="inner-title abs" style="left:130px;top:264px">MAJOR PROJECTS<br>COMPLETED</div>
  <ul class="bullets abs" style="left:124px;top:300px;width:142px">
    <li><b>675 TR, 1960 HP</b> ammonia refrigeration system for a bakery.</li>
    <li><b>90 TR, 400 HP</b> freon spiral blast freezer for meat processing plant.</li>
    <li><b>920 TR, 1420 HP</b> ammonia refrigeration system for meat processing facility.</li>
    <li><b>1300 TR</b> freon chiller and glycol chiller and glycol distribution system for a dairy processing plant.</li>
    <li>An ammonia refrigeration system for 560,000 sq. ft cold storage and food distribution facility.</li>
    <li>480 ton ice production facility.</li>
    <li><b>375 TR, 1500 HP</b> ice-cream plant.</li>
  </ul>

  <div class="service-panel abs"></div>
  <div class="inner-title inner-title--light abs" style="left:308px;top:38px">SERVICE &amp; MAINTENANCE</div>
  <div class="emergency abs">
    <span>24 HOUR<br>EMERGENCY<br>SERVICE!</span>
    <svg width="30" height="30" viewBox="0 0 30 30" aria-hidden="true">
      <g stroke="var(--deep-blue)" stroke-width="3.5" stroke-linecap="round">
        <line x1="5" y1="25" x2="22" y2="8"/><line x1="6" y1="6" x2="25" y2="25"/>
      </g>
      <circle cx="23" cy="7" r="4.5" fill="none" stroke="var(--deep-blue)" stroke-width="2.5"/>
    </svg>
  </div>
  <ul class="checks checks--light abs" style="left:302px;top:61px;width:241px">
    <li>Ammonia and Freon.</li>
    <li>Customized maintenance program.</li>
    <li>Troubleshooting service and repair of refrigeration and HVAC systems including all mechanical, structural, electrical and control components.</li>
    <li>Compressor rebuilding as well as vibration and oil analysis,</li>
    <li>Refrigerant conversion and recovery.</li>
    <li>Build-up ammonia and freon refrigeration systems, packaged freon refrigeration units, blast freezing/cooling systems, spiral and tunnel freezers, holding freezers and coolers, evaporators, glycol and water chillers, ice production machines, process rooms.</li>
    <li>Compressors, evaporative and air-cool condensers, recirculation packages, ammonia, water and glycol pumps, heat exchangers, control valves and regulators, electrical motors.</li>
    <li>Safety devices test, repair and calibration including: relief valves, leak detectors, pressure and temperature sensors, level switches and interlock devices.</li>
    <li>Packaged and split gas/electric air conditioners, heat pumps.</li>
    <li>Air handlers, exhaust fans, swamp coolers, water chillers, water towers and pumps.</li>
    <li>Exhaust and ventilation, humidification and dehumidification, clean rooms.</li>
    <li>Boilers and Boiler Piping.</li>
    <li>Refrigeration and Building Control and automation.</li>
    <li>PLC, VFD, VSD, VAV.</li>
  </ul>

  <div class="inner-title abs" style="left:591px;top:38px">ENGINEERING SERVICES</div>
  <ul class="checks checks--dark abs" style="left:588px;top:61px;width:222px">
    <li>Design ammonia and freon systems.</li>
    <li>Buildup and packaged refrigeration systems.</li>
    <li>Liquid recirculating, flooded, and DX systems.</li>
    <li>Low and high temperature chillers.</li>
    <li>Glycol and chill water distribution systems.</li>
    <li>Energy saving and expansion projects.</li>
    <li><b>3D solid modeling</b> and <b>2D CAD</b> drawings.</li>
    <li>Computerized control design and implementation, <b>PLC, VFD.</b></li>
    <li>Mechanical integrity surveys, safety and hazard analysis, seismic assessment.</li>
    <li>Safety programs, <b>PSM, RMP, CalARP, MOC, SOP.</b></li>
    <li>Regulatory Compliance and Professional training.</li>
    <li><span class="hl">Free survey &amp; quote</span> on your refrigeration and air conditioning equipment needs.</li>
  </ul>

  <div class="inner-title abs" style="left:591px;top:258px">COMPANIES WE PROUDLY SERVE</div>
  <div class="clients abs">
    <span>Grainfield</span><span>Valecrest Hospital</span><span>Nordia</span><span>Sunspoon</span><span>City Works</span>
    <span>Frostia</span><span>Oakridge Clinic</span><span>Nordale</span><span>Bulkmart</span><span>Fizzco</span>
    <span>Eastgate Foods</span><span>Chillwell</span><span>Coldline</span><span>Burgerly</span><span>Sodaria</span>
    <span>Brightwave</span><span>Pepperfizz</span><span>Trailhouse</span><span>Meadowvale</span><span>Quantel</span>
  </div>

  <div class="promise abs">
    <p>CUSTOMER SATISFACTION<br>IS OUR<br>ULTIMATE GOAL!</p>
    <p class="url">www.summitcoolair.com</p>
  </div>
</section>

</body>
</html>
```